HR services to some of biggest Silicon Valley Tech companies needs a new website

We need a new website design probably 4-5 pages initially. Here are some websites we like the look of https://quillmarkgroup.example/ , https://www.vantrel.example/ and https://pemvio.example/ .

Target Market(s)

Silicon valley tech companies

Industry/Entity Type

HR

Coding

Coded - Design and coding required

Number of Pages Required

5+ page

Requirements
Nice to have
• any stock photos or images should show a diverse group of people. Our client base is very diverse

```html
<!DOCTYPE html>
<html lang="en">
<head>
<meta charset="utf-8">
<title>Kestrel HR Consulting</title>
<link href="https://fonts.googleapis.com/css2?family=Jura:wght@500;600;700&family=Roboto:wght@400;500&family=Roboto+Condensed:wght@500;700&display=swap" rel="stylesheet">
<style>
:root{
  --yellow:#f7c316;
  --dark:#4a4a4d;
  --darker:#2d2d30;
  --footer:#2a2a2d;
  --bar:#1f1f21;
  --ink:#222;
  --muted:#555;
  --white:#fff;
  --field:#f0f0f0;
}
*{margin:0;padding:0;box-sizing:border-box}
html,body{width:1200px;height:4271px;overflow:hidden}
body{position:relative;background:var(--white);font-family:'Roboto',sans-serif;color:var(--ink)}
.abs{position:absolute}
.display{font-family:'Jura',sans-serif;font-weight:600}
.btn{position:absolute;background:var(--yellow);color:var(--ink);font-family:'Roboto Condensed',sans-serif;font-weight:700;font-size:14px;display:flex;align-items:center;justify-content:center;letter-spacing:.2px}
.divider{position:absolute;left:50%;transform:translateX(-50%);height:2px}
.divider.light{background:var(--yellow)}
.divider.onDark{background:var(--white)}

/* hero */
.hero-photo{left:0;top:0;width:1200px;height:700px;background:linear-gradient(110deg,#3a332c 0%,#7a6652 35%,#a58c70 55%,#6f6050 80%,#4b4239 100%)}
.topnav{left:0;top:71px;width:1200px;height:48px;background:var(--white)}
.nav{right:62px;top:86px;display:flex;gap:18px;font-family:'Roboto Condensed',sans-serif;font-weight:500;font-size:14px;color:#222}
.logo-flag{left:111px;top:0;width:146px;height:196px}
.logo-text{left:111px;top:82px;width:146px;text-align:center;color:var(--white);font-family:'Jura',sans-serif;font-weight:700;font-size:17px;line-height:1.05;letter-spacing:1px}
.logo-text small{display:block;font-size:11px;letter-spacing:3px}
.logo-mark{left:170px;top:42px;width:28px;height:28px;border:3px solid var(--white);border-radius:50%}
.appt{left:862px;top:13px;width:223px;height:47px;justify-content:flex-start;padding-left:22px;font-size:14px}
.appt .arrow{position:absolute;right:12px;top:10px;width:28px;height:27px;background:var(--white);display:flex;align-items:center;justify-content:center}
.hero-title{left:109px;top:258px;color:var(--white);font-size:44px;line-height:55px;font-weight:600;letter-spacing:1px}
.hero-sub{left:111px;top:402px;color:var(--white);font-family:'Roboto Condensed',sans-serif;font-weight:500;font-size:20px}
.hero-btn{left:111px;top:469px;width:146px;height:46px}
.play{left:871px;top:303px;width:100px;height:100px}

/* about */
.about-bg{left:0;top:580px;width:1200px;height:830px}
.about-title{left:110px;top:812px;color:var(--yellow);font-size:37px}
.about-p{left:108px;color:var(--white);font-size:15.5px;line-height:30px;width:460px}
.about-h{left:108px;top:1013px;color:var(--white);font-size:21px;font-family:'Roboto',sans-serif;font-weight:400}
.about-btn{left:111px;top:1186px;width:146px;height:47px}

/* services */
.section-title{left:0;width:1200px;text-align:center;font-size:35px;font-weight:600;letter-spacing:1.5px}
.cards{left:0;top:1579px;width:1200px;height:459px;display:flex}
.card{width:300px;height:459px;position:relative;color:var(--white);padding:0 20px 0 33px}
.card.photo-a{background:linear-gradient(160deg,#55555a,#3c3c40)}
.card.photo-b{background:linear-gradient(160deg,#6a6a6e,#48484c)}
.card.photo-c{background:linear-gradient(160deg,#5d5d62,#404044)}
.card.feature{background:var(--yellow);color:var(--ink)}
.card svg{position:absolute;left:33px;top:50px}
.card h3{position:absolute;left:33px;top:120px;font-family:'Jura',sans-serif;font-weight:600;font-size:27px;line-height:30px;letter-spacing:.5px}
.card ul{position:absolute;left:33px;right:14px;list-style:none;font-size:14.5px;line-height:30px}
.card li{position:relative;padding-left:21px}
.card li::before{content:"";position:absolute;left:0;top:10px;width:10px;height:10px;border-radius:50%;background:currentColor}
.card li::after{content:"";position:absolute;left:3px;top:13px;width:4px;height:2px;border-left:1.5px solid #555;border-bottom:1.5px solid #555;transform:rotate(-45deg)}
.card.feature li::after{border-color:var(--yellow)}

/* team */
.team-bg{left:0;top:2210px;width:1200px;height:728px;background:linear-gradient(#f6f6f6,#ffffff 40%)}
.team-intro{left:160px;top:2372px;width:880px;text-align:center;font-size:15.5px;line-height:30px;color:#333}
.member{width:220px;text-align:center}
.avatar{width:162px;height:162px;border-radius:50%;margin:0 auto;border:4px solid #555;background:linear-gradient(150deg,#9a9a9a,#4a4a4a)}
.avatar.lead{border-color:var(--yellow);background:linear-gradient(150deg,#7c7a60,#3e3d30)}
.member h4{font-family:'Jura',sans-serif;font-weight:600;font-size:22px;margin-top:25px;letter-spacing:.5px}
.member p{font-size:19px;margin-top:8px;color:#333}

/* testimonials */
.testi-bg{left:0;top:2938px;width:1200px;height:379px;background:var(--darker)}
.testi-title{color:var(--yellow)}
.quote-text{left:160px;top:3165px;width:880px;text-align:center;color:var(--white);font-size:16.5px;line-height:30px}
.dots{left:559px;top:3254px;display:flex;gap:5px}
.dots span{width:13px;height:13px;border-radius:50%;border:1.5px solid #bbb}
.dots span.on{background:var(--white);border-color:var(--white)}

/* contact */
.contact-title{left:110px;top:3427px;color:var(--yellow);font-size:37px}
.contact-p{left:110px;top:3490px;width:480px;font-size:16.5px;line-height:30px;color:#333}
.contact-row{left:108px;display:flex;align-items:center;gap:18px;font-size:16.5px;color:#222}
.contact-row svg{width:34px;flex:none}
.form-card{left:610px;top:3405px;width:479px;height:361px;background:var(--white);box-shadow:0 4px 22px rgba(0,0,0,.14)}
.form-card h5{position:absolute;left:38px;top:30px;font-size:15.5px;font-weight:500}
.field{position:absolute;background:var(--field);font-size:13px;color:#777;padding:14px 20px}
.form-btn{left:38px;top:285px;width:401px;height:45px;font-size:14px}

/* footer */
.footer-links{color:var(--white)}
.footer-links h6{font-family:'Roboto',sans-serif;font-weight:500;font-size:16.5px;margin-bottom:14px}
.footer-links li{list-style:none;font-size:14.5px;line-height:30px}
.foot-logo{left:109px;top:4010px;color:var(--white);font-family:'Jura',sans-serif;font-weight:700;font-size:29px;line-height:1.05;letter-spacing:1.5px}
.foot-logo small{display:block;font-size:17px;letter-spacing:6px}
.foot-mark{left:180px;top:3985px;width:20px;height:20px;border:3px solid var(--yellow);border-radius:50%}
.foot-btn{left:109px;top:4144px;width:183px;height:47px}
.bar{left:0;top:4217px;width:1200px;height:54px;background:var(--bar)}
.copyright{left:111px;top:4236px;color:#ddd;font-size:15.5px}
.social{left:925px;top:4238px;display:flex;gap:36px}
.social span{width:12px;height:12px;border-radius:50%;background:#ddd}
</style>
</head>
<body>

<!-- HERO -->
<div class="abs hero-photo" role="img" aria-label="Photo of a diverse team of smiling office colleagues standing together"></div>
<div class="abs topnav"></div>
<nav class="abs nav"><span>HOME</span><span>WHAT WE DO</span><span>HOW IT WORKS</span><span>OUR CLIENTS</span><span>ABOUT US</span><span>BLOG</span></nav>
<svg class="abs logo-flag" viewBox="0 0 146 196"><polygon points="0,0 146,0 146,150 73,196 0,150" fill="#f7c316"/></svg>
<div class="abs logo-mark"></div>
<div class="abs logo-text">KESTREL HR<small>CONSULTING</small></div>
<div class="btn appt">MAKE APPPOINTMENT<span class="arrow"><svg width="16" height="12" viewBox="0 0 16 12"><path d="M0 6h14M9 1l5 5-5 5" stroke="#222" stroke-width="2" fill="none"/></svg></span></div>
<h1 class="abs display hero-title">Kestrel HR Consulting is the<br>solution to all your HR issues.</h1>
<p class="abs hero-sub">A ONE-STOP-SHOP PROVIDING A VARIETY OF SERVICES</p>
<div class="btn hero-btn">LEARN MORE</div>
<svg class="abs play" viewBox="0 0 100 100"><circle cx="50" cy="50" r="48" fill="none" stroke="#fff" stroke-width="2.5"/><polygon points="40,33 68,50 40,67" fill="#fff"/></svg>

<!-- ABOUT -->
<svg class="abs about-bg" viewBox="0 0 1200 830" preserveAspectRatio="none">
  <polygon points="0,16 199,108 1200,0 1200,830 0,830" fill="#4a4a4d"/>
  <polyline points="0,16 199,108 1200,0" fill="none" stroke="#f7c316" stroke-width="4"/>
</svg>
<h2 class="abs display about-title">About Kestrel HR</h2>
<p class="abs about-p" style="top:871px">Kestrel HR Consulting is the solution to all your HR issues. We are a one-stop-shop providing a variety of services. Whether you have a specific HR need or seek relief by outsourcing altogether, we have you covered.</p>
<h3 class="abs about-h">15 YEARS IN BUSINESS</h3>
<p class="abs about-p" style="top:1056px">For fifteen years our team of industry experts has been providing HR consulting services with innovative strategies and a partnership mentality</p>
<div class="btn about-btn">LEARN MORE</div>
<svg class="abs" style="left:610px;top:735px" width="500" height="500" viewBox="0 0 500 500">
  <circle cx="247" cy="248" r="244" fill="none" stroke="#f7c316" stroke-width="2"/>
</svg>
<div class="abs" role="img" aria-label="Photo of colleagues discussing work at a bright office table" style="left:630px;top:756px;width:454px;height:454px;border-radius:50%;background:linear-gradient(140deg,#d9d6cf,#8f8a80)"></div>
<div class="abs" role="img" aria-label="Photo of a smiling woman working at a laptop" style="left:594px;top:1068px;width:274px;height:274px;border-radius:50%;border:6px solid #fff;background:linear-gradient(150deg,#7d8da0,#3e4856)"></div>

<!-- SERVICES -->
<h2 class="abs display section-title" style="top:1462px">Services We Provide</h2>
<div class="divider light" style="top:1520px;width:240px"></div>

<div class="abs cards">
  <div class="card photo-a" role="img" aria-label="Photo of a smiling woman in an office, darkened behind the text">
    <svg width="50" height="50" viewBox="0 0 50 50" fill="none" stroke="#fff" stroke-width="2"><circle cx="25" cy="25" r="9"/><circle cx="25" cy="25" r="17" stroke-dasharray="6 4"/><path d="M8 42l14-14"/></svg>
    <h3>Setup</h3>
    <ul style="top:163px"><li>Select and implement an HRIS system</li><li>Create Company Handbook</li><li>Write termination procedure</li><li>Set up benefits services</li><li>Set up workers comp vendor</li><li>Create job descriptions for current and anticipated roles</li></ul>
  </div>
  <div class="card photo-b" role="img" aria-label="Photo of a man in glasses working on a laptop, darkened behind the text">
    <svg width="50" height="50" viewBox="0 0 50 50" fill="none" stroke="#fff" stroke-width="2"><path d="M42 25a17 17 0 0 1-29 12M8 25a17 17 0 0 1 29-12"/><path d="M37 6v7h-7M13 44v-7h7"/></svg>
    <h3>Recurring<br>Procedures</h3>
    <ul style="top:193px"><li>Review handbook annually</li><li>Roll out training</li><li>Write offer letters</li><li>Handle employee data and files</li><li>Conduct I-9 audits</li><li>Handle merit and review bonuses</li></ul>
  </div>
  <div class="card feature">
    <svg width="56" height="56" viewBox="0 0 56 56" fill="none" stroke="#222" stroke-width="2"><circle cx="18" cy="18" r="8"/><circle cx="36" cy="14" r="5"/><path d="M6 44h14l12-6h14M6 52h40"/></svg>
    <h3>Managing HR<br>Functions</h3>
    <ul style="top:193px"><li>Onboarding/Offboarding</li><li>Employee relations</li><li>Investigations</li><li>Leave administration</li><li>Immigration liaison</li><li>Compensation management</li><li>Full cycle recruitment</li></ul>
  </div>
  <div class="card photo-c" role="img" aria-label="Photo of a man using a tablet, darkened behind the text">
    <svg width="60" height="50" viewBox="0 0 60 50" fill="none" stroke="#fff" stroke-width="2"><path d="M4 4h30v20H16l-8 7v-7H4z"/><path d="M40 16h16v20h-4v7l-8-7H24v-6"/><circle cx="12" cy="14" r="1.5" fill="#fff"/><circle cx="19" cy="14" r="1.5" fill="#fff"/><circle cx="26" cy="14" r="1.5" fill="#fff"/></svg>
    <h3>Partner<br>Communications</h3>
    <ul style="top:193px"><li>Manage annual bidding process for benefits review</li><li>Handle workers compensation claims administration</li><li>Manage leave administration</li><li>Handle EDD inquires</li><li>Partner on M&amp;A activity</li></ul>
  </div>
</div>
<div class="btn" style="left:509px;top:2122px;width:182px;height:46px">VIEW ALL SERVICES</div>

<!-- TEAM -->
<div class="abs team-bg"></div>
<h2 class="abs display section-title" style="top:2265px">Meet Our Team</h2>
<div class="divider light" style="top:2324px;width:220px"></div>
<p class="abs team-intro">Our team is woman-owned, women-led and partnership-oriented. Working with us means you're hiring senior-level talent that acts as an extension of your company.</p>
<div class="abs member" style="left:86px;top:2512px"><div class="avatar lead" role="img" aria-label="Portrait photo of the CEO"></div><h4>Dorian Vale</h4><p>CEO</p></div>
<div class="abs member" style="left:359px;top:2512px"><div class="avatar" role="img" aria-label="Black and white portrait photo of an HR expert"></div><h4>Imani Rhodes</h4><p>HR Expert</p></div>
<div class="abs member" style="left:622px;top:2512px"><div class="avatar" role="img" aria-label="Black and white portrait photo of an HR expert"></div><h4>Kenji Arlow</h4><p>HR Expert</p></div>
<div class="abs member" style="left:893px;top:2512px"><div class="avatar" role="img" aria-label="Black and white portrait photo of an HR expert"></div><h4>Selene</h4><p>HR Expert</p></div>
<div class="btn" style="left:509px;top:2842px;width:182px;height:46px">MEET OUR TEAM</div>

<!-- TESTIMONIALS -->
<div class="abs testi-bg"></div>
<h2 class="abs display section-title testi-title" style="top:2965px">Testimonials</h2>
<div class="divider onDark" style="top:3023px;width:220px"></div>
<svg class="abs" style="left:573px;top:3080px" width="54" height="54" viewBox="0 0 54 54"><circle cx="27" cy="27" r="25.5" fill="none" stroke="#f7c316" stroke-width="2"/><text x="27" y="38" text-anchor="middle" font-family="Georgia,serif" font-size="28" font-weight="700" fill="#f7c316">&#8220;</text></svg>
<p class="abs quote-text">"Sed ut perspiciatis unde omnis iste natus error sit voluptatem accusantium doloremque laudantium, totam rem aperiam, eaque ipsa quae ab illo inventore veritatis et quasi architecto beatae vitae dicta sunt explicabo."</p>
<div class="abs dots"><span></span><span></span><span class="on"></span><span></span><span></span></div>

<!-- CONTACT -->
<h2 class="abs display contact-title">Contact Us</h2>
<p class="abs contact-p">Sed ut perspiciatis unde omnis iste natus error sit voluptatem accusantium doloremque laudantium.</p>
<div class="abs contact-row" style="top:3593px"><svg height="32" viewBox="0 0 34 32"><path d="M17 1a10 10 0 0 0-10 10c0 8 10 20 10 20s10-12 10-20A10 10 0 0 0 17 1z" fill="#222"/><circle cx="17" cy="11" r="4" fill="#fff"/></svg>Kestrel HR, 123 street, demo address.</div>
<div class="abs contact-row" style="top:3653px"><svg height="32" viewBox="0 0 34 32"><path d="M6 2l6 0 3 8-4 3c2 4 5 7 9 9l3-4 8 3v6c0 2-2 3-4 3C15 29 3 17 3 5c0-2 1-3 3-3z" fill="#222"/></svg>555-014-2837</div>
<div class="abs contact-row" style="top:3714px"><svg height="26" viewBox="0 0 34 26"><rect x="1" y="1" width="32" height="24" fill="#222"/><path d="M1 2l16 12L33 2" fill="none" stroke="#fff" stroke-width="2"/></svg>info@kestrelhr.example</div>

<div class="abs form-card">
  <h5>Book An Appointment</h5>
  <div class="field" style="left:38px;top:71px;width:199px;height:45px">Name</div>
  <div class="field" style="left:241px;top:71px;width:199px;height:45px">Phone</div>
  <div class="field" style="left:38px;top:125px;width:199px;height:45px">Email</div>
  <div class="field" style="left:241px;top:125px;width:199px;height:45px">Date</div>
  <div class="field" style="left:38px;top:176px;width:402px;height:88px">Message</div>
  <div class="btn form-btn">BOOK AN APPOINTMENT</div>
</div>

<!-- FOOTER -->
<svg class="abs" style="left:0;top:3840px" width="1200" height="380" viewBox="0 0 1200 380" preserveAspectRatio="none">
  <polygon points="0,122 1000,8 1200,110 1200,380 0,380" fill="#f7c316"/>
  <polygon points="0,128 1000,36 1200,150 1200,380 0,380" fill="#2a2a2d"/>
</svg>
<div class="abs foot-mark"></div>
<div class="abs foot-logo">KESTREL HR<small>CONSULTING</small></div>
<div class="btn foot-btn">CONTACT US</div>
<div class="abs footer-links" style="left:411px;top:3993px"><h6>LINKS</h6><ul><li>HOME</li><li>WHAT WE DO</li><li>HOW IT WORKS</li><li>OUR CLIENTS</li><li>ABOUT US</li></ul></div>
<div class="abs footer-links" style="left:631px;top:3993px"><h6>SERVICES</h6><ul><li>SETUP</li><li>RECURRING PROCEDURES</li><li>MANAGING HR FUNCTIONS</li><li>PARTNER COMMUNICATION</li></ul></div>
<div class="abs footer-links" style="left:918px;top:3993px"><h6>OTHERS</h6><ul><li>PRIVACY POLICY</li><li>TEARMS &amp; CONDITIONS</li><li>FAQS</li><li>BLOG</li></ul></div>
<div class="abs bar"></div>
<p class="abs copyright">2021 Kestrel HR Consulting. All Rights Reserved.</p>
<div class="abs social"><span></span><span></span><span></span><span></span></div>

</body>
</html>
```